Photon Clash's Website Redesign.

Photon Clash is an Indoor Laser Tag chain that is based in Malaysia.
We would like to revamp our current design.

Current website is www.glowarenaplay.com.my

More pictures can be found in our facebook
www.facebook.com/glowarenaplay
www.facebook.com/photonclashsouth

You can use whatever pictures and materials found in current website and facebook for the proposal. More graphics can be provided later on when we are satisfied with the design. Please feel free to ask more questions.

Website should have:

1. A contact form.
2. Interface to display twitter updates.
3. Links to facebook.
4. Content management system
5. Integration to Google Maps to show location of branches.

Derek

Target Market(s)

13 years old to 35 years old.
Corporates.

Font styles to use
Serif
Sans Serif

Colors
eb1f27
0255a3

Requirements
Must have
• 1. A contact form.
• 2. Interface to display twitter updates.
• 3. Links to facebook.
• 4. Content management system
• 5. Integration to Google Maps to show location of branches.
Nice to have
• Open to suggestions

```html
<!DOCTYPE html>
<html lang="en">
<head>
<meta charset="utf-8">
<title>Photon Clash – Indoor Laser Tag</title>
<link href="https://fonts.googleapis.com/css2?family=Arimo:wght@400;700&display=swap" rel="stylesheet">
<style>
:root{
  --navy-deep:#03124a;
  --navy:#0a2378;
  --blue:#0255a3;
  --blue-bright:#1f6fd6;
  --blue-light:#4ea3f0;
  --panel:#0b1b52;
  --panel-dark:#061238;
  --red:#eb1f27;
  --white:#ffffff;
  --ink:#222222;
  --grey:#e9ecf2;
  --muted:#9fb4da;
}
*{box-sizing:border-box;margin:0;padding:0}
html,body{width:672px;height:1200px;overflow:hidden}
body{
  font-family:"Arimo",Arial,sans-serif;
  background:linear-gradient(180deg,var(--navy-deep) 0,var(--navy) 90px,var(--blue) 420px,#0a3c8f 1050px,var(--navy-deep) 1200px);
  color:var(--white);
  position:relative;
}
.page{position:absolute;left:0;top:0;width:672px;height:1200px}

/* header */
.site-header{position:absolute;left:0;top:0;width:672px;height:80px;
  background:linear-gradient(180deg,#0d2f8a,#06185a);border-bottom:1px solid #2a56b8}
.brand{position:absolute;left:282px;top:4px;width:108px;height:60px;border-radius:8px;
  background:linear-gradient(180deg,#ffffff,#c9d6ea);display:flex;align-items:center;justify-content:center;gap:5px}
.brand-dot{width:9px;height:9px;border-radius:50%;background:var(--blue)}
.brand-name{font-weight:700;font-size:13px;color:var(--blue)}
.phone{position:absolute;right:64px;top:14px;display:flex;align-items:center;gap:6px;font-size:15px;font-weight:700}
.phone svg{width:14px;height:14px}

/* nav */
.main-nav{position:absolute;left:96px;top:86px;width:522px;height:27px;
  background:linear-gradient(180deg,#2a63c4,#0c3490);border:1px solid #4a7ed6;display:flex}
.main-nav a{color:var(--white);text-decoration:none;font-size:8px;font-weight:700;
  flex:auto;display:flex;align-items:center;justify-content:center;border-right:1px solid #3f70c8;text-transform:uppercase}
.main-nav a:last-child{border-right:none}
.main-nav a.active{background:#0a2a78}

/* hero */
.hero{position:absolute;left:96px;top:113px;width:522px;height:155px;
  background:radial-gradient(ellipse at 55% 45%,#4f87c8 0,#1b3e78 45%,#06112f 100%);overflow:hidden}
.hero-arrow{position:absolute;top:66px;font-size:18px;font-weight:700;color:var(--white)}
.hero-arrow.prev{left:10px}.hero-arrow.next{right:10px}
.hero-dots{position:absolute;left:224px;bottom:10px;display:flex;gap:4px}
.hero-dots span{width:7px;height:7px;background:#8a8f9a}
.hero-dots span.on{background:var(--red)}
.hero-url{position:absolute;right:14px;bottom:8px;font-size:8px;font-weight:700;letter-spacing:.5px}
.hero-strip{position:absolute;left:96px;top:268px;width:522px;height:10px;background:var(--white)}

/* service boxes */
.services{position:absolute;left:96px;top:286px;width:522px;height:112px;
  background:linear-gradient(180deg,#2a5cb8,#1a3f92);border-radius:6px;display:flex;gap:6px;padding:8px 10px}
.service{flex:1;position:relative}
.service h2{height:18px;background:linear-gradient(180deg,#4a86e0,#1d54b4);font-size:11px;font-weight:400;
  text-align:center;line-height:18px;border-radius:3px 3px 0 0;text-transform:uppercase}
.service-body{height:60px;background:var(--panel-dark);display:flex;gap:8px;padding:8px}
.service-body svg{width:38px;height:38px;flex:none}
.service-body p{font-size:7.5px;line-height:9.5px}
.read-btn{position:absolute;right:4px;bottom:2px;font-size:6.5px;background:#08163f;border-radius:8px;
  padding:3px 8px 3px 14px;border:1px solid #3f6fc2}
.read-btn::before{content:"";position:absolute;left:4px;top:4px;width:6px;height:6px;border-radius:50%;background:var(--blue-light)}

/* main */
.content{position:absolute;left:96px;top:414px;width:522px;height:548px;display:flex;gap:8px;
  background:#0a2a7a;border-top:3px solid #c8862a;padding:4px 0 0 4px}
.article{width:342px;height:538px;background:var(--white);border-radius:8px;color:var(--ink);padding:10px 14px;position:relative}
.article h1{font-size:13px;font-weight:700;margin-bottom:8px}
.article h1 span{color:var(--red)}
.article p{font-size:6.6px;line-height:8.4px;margin-bottom:8px;color:#333}
.article p.indent{text-indent:10px}
.team-photo{display:block;width:272px;height:150px;margin:10px auto 12px;
  background:linear-gradient(180deg,#2d3a86,#b0426e 55%,#21244c)}
.gallery{background:var(--grey);margin:0 -14px;padding:6px 14px;height:148px}
.gallery h2{font-size:12px;font-weight:700;margin-bottom:6px}
.thumbs{display:grid;grid-template-columns:repeat(5,1fr);gap:8px 10px}
.thumbs span{height:42px;border:2px solid var(--white);box-shadow:0 0 2px #888;
  background:linear-gradient(135deg,#3a2a7a,#a83a6a)}
.thumbs span:nth-child(2n){background:linear-gradient(135deg,#1e3a8a,#7a3a9a)}
.view-all{position:absolute;right:26px;bottom:12px;font-size:7px;color:var(--blue);text-decoration:underline}

.sidebar{width:164px;display:flex;flex-direction:column;gap:6px}
.widget{background:var(--panel-dark);border:1px solid #2a4e9e}
.widget h3{font-size:8.5px;font-weight:400;background:linear-gradient(180deg,#3a72d0,#1a4aa8);padding:4px 6px;text-transform:uppercase}
.widget-row{display:flex;gap:6px;padding:6px}
.pic{flex:none;background:linear-gradient(160deg,#2a5a8a,#0e1f40)}
.widget p{font-size:6.5px;line-height:8px}
.btn{display:inline-block;font-size:6.5px;background:#1e52b0;padding:3px 8px;border-radius:3px}
.post-title{font-size:8px;font-weight:700;padding:6px 6px 0}
.post-date{font-size:6px;padding:2px 6px 0}
.news-item{display:flex;gap:6px;padding:5px 6px;border-bottom:1px solid #1b2f66}
.news-item .pic{width:26px;height:24px;background:linear-gradient(135deg,#e9a33a,#3aa35a)}
.news-item b{display:block;font-size:6px;color:var(--blue-light);font-weight:400}
.news-item i{font-style:normal;font-size:5.5px;display:block}
.news-item small{display:block;font-size:5.5px;color:var(--muted)}

/* testimonials */
.testimonials{position:absolute;left:96px;top:968px;width:522px;height:86px;background:var(--panel-dark);padding:6px 12px}
.testimonials h2{font-size:9px;font-weight:400;color:var(--blue-light);margin-bottom:8px}
.quotes{display:flex;gap:14px}
.quote{flex:1;display:flex;gap:6px}
.avatar{width:26px;height:26px;border-radius:50%;background:linear-gradient(180deg,#c9b9a8,#6a5a4a);flex:none;border:2px solid var(--white)}
.quote p{font-size:6.5px;line-height:8px}
.quote cite{display:block;font-style:normal;font-size:6.5px;margin-top:6px}
.quote-nav{position:absolute;right:10px;bottom:6px;font-size:9px;font-weight:700}

/* footer */
.site-footer{position:absolute;left:96px;top:1058px;width:522px;height:120px;display:flex;gap:10px;padding:6px 8px}
.f-col{width:112px}
.f-col h4{font-size:9px;font-weight:700;margin-bottom:5px}
.f-col ul{list-style:none;font-size:6.5px;line-height:8.2px}
.tweet{font-size:6px;line-height:7.4px;margin-bottom:4px}
.tweet em{font-style:normal;color:var(--blue-light)}
.social{display:flex;gap:4px;margin-top:4px}
.social span{width:10px;height:10px}
.newsletter{width:160px;background:linear-gradient(180deg,#1a4aa8,#0a2a78);border-radius:6px;padding:5px 6px;position:relative}
.newsletter .tag{display:inline-block;background:#0a1a4a;font-size:7px;padding:2px 6px;margin-bottom:5px;letter-spacing:.5px}
.newsletter p{font-size:6.5px;margin-bottom:4px;padding-left:16px;position:relative}
.newsletter p svg{position:absolute;left:0;top:-2px;width:12px;height:10px}
.newsletter .field{background:var(--white);color:#666;font-size:6px;padding:3px 4px;border-radius:2px;margin-bottom:4px}
.newsletter .submit{display:block;width:52px;margin-left:auto;background:#08163f;font-size:7px;font-weight:700;text-align:center;padding:3px 0;border-radius:8px}
.copyright{position:absolute;left:0;top:1180px;width:672px;height:20px;font-size:7px;text-align:center;line-height:20px;background:var(--navy-deep)}
</style>
</head>
<body>
<div class="page">

<header class="site-header">
  <div class="brand"><span class="brand-dot"></span><span class="brand-name">Photon Clash</span></div>
  <div class="phone">
    <svg viewBox="0 0 24 24"><path fill="#4ea3f0" d="M6.6 10.8a15.1 15.1 0 0 0 6.6 6.6l2.2-2.2a1 1 0 0 1 1-.25 11.4 11.4 0 0 0 3.6.6 1 1 0 0 1 1 1V20a1 1 0 0 1-1 1A17 17 0 0 1 3 4a1 1 0 0 1 1-1h3.5a1 1 0 0 1 1 1c0 1.25.2 2.45.6 3.6a1 1 0 0 1-.25 1z"/></svg>
    888 - 2290 - 5561
  </div>
</header>

<nav class="main-nav">
  <a class="active" href="#">Home</a><a href="#">Photo Gallery</a><a href="#">FAQ's</a><a href="#">Contact Us</a><a href="#">Outdoor Laser Tag</a><a href="#">Comparison of Features</a><a href="#">Online Booking</a>
</nav>

<section class="hero" role="img" aria-label="Slide: laser tag arena artwork with game title and warning sign">
  <span class="hero-arrow prev">‹</span><span class="hero-arrow next">›</span>
  <div class="hero-dots"><span class="on"></span><span></span><span></span></div>
  <div class="hero-url">www.glowarenaplay.com.my</div>
</section>
<div class="hero-strip"></div>

<section class="services">
  <div class="service">
    <h2>Who we are</h2>
    <div class="service-body">
      <svg viewBox="0 0 40 40"><circle cx="20" cy="12" r="6" fill="#4ea3f0"/><path d="M8 34c0-8 5-13 12-13s12 5 12 13z" fill="#4ea3f0"/></svg>
      <p>Lorem ipsum dolor sit amet, consectetur adipiscing elit. Sed diam nonum...</p>
    </div>
    <span class="read-btn">Read more</span>
  </div>
  <div class="service">
    <h2>What we do</h2>
    <div class="service-body">
      <svg viewBox="0 0 40 40"><circle cx="14" cy="11" r="5" fill="#4ea3f0"/><path d="M4 34c0-7 4-12 10-12s8 4 9 8h13v4z" fill="#4ea3f0"/></svg>
      <p>Lorem ipsum dolor sit amet, consectetur adipiscing elit. Sed diam nonum...</p>
    </div>
    <span class="read-btn">Read more</span>
  </div>
  <div class="service">
    <h2>Our business</h2>
    <div class="service-body">
      <svg viewBox="0 0 40 40"><path d="M3 18l9-6 8 5 8-5 9 6-9 10-8-5-8 5z" fill="#4ea3f0"/></svg>
      <p>Lorem ipsum dolor sit amet, consectetur adipiscing elit. Sed diam nonum...</p>
    </div>
    <span class="read-btn">Read more</span>
  </div>
</section>

<main class="content">
  <article class="article">
    <h1>Welcome to <span>Photonclashplay.com.my</span></h1>
    <p>Lorem ipsum dolor sit amet, consectetur adipiscing elit. Sed diam nonumy in convallis gravida neque. Nulla gravida vestibulum mattis a accumsan, aliquam in sagittis at. Sollicitudin sed massa ut enim veniam. Curabitur tempus sem vitae mi vestibulum volutpat malesuada erat vestibulum. Sed aliquam dolor at dolor consec quat gravida. Fusce nimeque tempus nec feugiat sit amet. Tincidunt ut leo. Nam semper ornare enim.</p>
    <p>Lorem ipsum dolor sit amet, consectetur adipiscing elit. Sed diam nonumy inconvalls gravida neque. Nulla gravida vestibulum mattis a accumsan, aliquam in sagittis at. Sollicitudin sed massa ut enim veniam. Curabitur tempus sem vitae mi vestibulum volutpat malesuada erat vestibulum. Sed aliquam dolor at dolor consequat gravida. Fusce nimeque tempus nec feugiat sit amet. Tincidunt ut leo. Nam semper ornare enim.</p>
    <p class="indent">Lorem ipsum dolor sit amet, consectetur adipiscing elit. Sed diam nonumy in convallis gravida neque. Nulla gravida vestibulum mattis a accumsan, aliquam in sagittis at. Sollicitudin sed massa ut enim veniam. Curabitur tempus sem vitae mi vestibulum volutpat malesuada erat vestibulum, sit at quam dolor at dolor consequat gravida. Fusce nimeque tempus nec feugiat sit amet. Tincidunt ut leo. Nam semper ornare enim.</p>
    <p class="indent">Lorem ipsum dolor sit amet, consectetur adipiscing elit. Sed diam nonumy inconvalls gravida neque. Nulla gravida vestibulum mattis a accumsan, aliquam in sagittis at. Sollicitudin sed massa ut nim veniam.</p>
    <div class="team-photo" role="img" aria-label="Group photo of players holding laser tag blasters in the arena"></div>
    <section class="gallery">
      <h2>Gallery Photos</h2>
      <div class="thumbs" role="img" aria-label="Ten thumbnail photos of laser tag games">
        <span></span><span></span><span></span><span></span><span></span>
        <span></span><span></span><span></span><span></span><span></span>
      </div>
    </section>
    <a class="view-all" href="#">View all</a>
  </article>

  <aside class="sidebar">
    <section class="widget">
      <h3>About us</h3>
      <div class="widget-row">
        <div class="pic" style="width:58px;height:58px" role="img" aria-label="Player aiming a laser tag blaster"></div>
        <div><p>Lorem ipsum dolor sit amet, consectetur adipiscing elit. Sed diam nonumy in convallis gravida neque.</p>
          <div style="text-align:right;margin-top:4px"><span class="btn">Read more</span></div></div>
      </div>
    </section>
    <section class="widget">
      <h3>Recent blog posts</h3>
      <div class="post-title">Lorem ipsum dolor sit amet, consectetuer</div>
      <div class="post-date">July, 5th, 2014</div>
      <div class="widget-row">
        <div class="pic" style="width:58px;height:58px" role="img" aria-label="Player in the laser tag arena"></div>
        <p>Lorem ipsum dolor sit amet, consectetur adipiscing elit. Sed diam nonumy in convallis gravida neque. Nulla gravida vesti bulum mattis a accumsan, aliquam in sagittis ut. Sed citudin sed massa ut enim veniam. Curabitur tempus sem vitae mi vesti bulum volutpat.</p>
      </div>
      <div style="display:flex;justify-content:space-between;padding:0 6px 6px"><span class="btn">More posts</span><span class="btn" style="background:none">read more</span></div>
    </section>
    <section class="widget">
      <h3>Latest news &amp; events</h3>
      <div class="news-item"><div class="pic" role="img" aria-label="Event thumbnail"></div><div><b>Lorem ipsum dolor sit amet, Cus tectetur adipiscing elit.</b><i>January, 13th 2014.</i><small>Lorem ipsum dolor sit amet, consect...</small></div></div>
      <div class="news-item"><div class="pic" role="img" aria-label="Event thumbnail"></div><div><b>Lorem ipsum dolor sit amet, Cus tectetur adipiscing elit.</b><i>January, 13th 2014.</i><small>Lorem ipsum dolor sit amet, consect...</small></div></div>
      <div class="news-item"><div class="pic" role="img" aria-label="Event thumbnail"></div><div><b>Lorem ipsum dolor sit amet, Cus tectetur adipiscing elit.</b><i>January, 13th 2014.</i><small>Lorem ipsum dolor sit amet, consect...</small></div></div>
      <div class="news-item"><div class="pic" role="img" aria-label="Event thumbnail"></div><div><b>Lorem ipsum dolor sit amet, Cus tectetur adipiscing elit.</b><i>January, 13th 2014.</i><small>Lorem ipsum dolor sit amet, consect...</small></div></div>
      <div style="text-align:right;padding:4px 6px;font-size:6.5px">View All</div>
    </section>
  </aside>
</main>

<section class="testimonials">
  <h2>What Customers Say</h2>
  <div class="quotes">
    <div class="quote"><div class="avatar" role="img" aria-label="Customer portrait"></div><div><p>"Lorem ipsum dolor sit amet, consectetur adipiscing elit. Sed diam nonumy inconvalls gravida neque."</p><cite>Adam Lee, Perak</cite></div></div>
    <div class="quote"><div class="avatar" role="img" aria-label="Customer portrait"></div><div><p>"Lorem ipsum dolor sit amet, consectetur adipiscing elit. Sed diam nonumy inconvalls gravida neque."</p><cite>Rina Hasan, KualaLumpur</cite></div></div>
    <div class="quote"><div class="avatar" role="img" aria-label="Customer portrait"></div><div><p>"Lorem ipsum dolor sit amet, consectetur adipiscing elit. Sed diam nonumy inconvalls gravida neque."</p><cite>Kevin Tan, Pahang</cite></div></div>
  </div>
  <span class="quote-nav">‹ ›</span>
</section>

<footer class="site-footer">
  <div class="f-col">
    <h4>Twitter Feed</h4>
    <p class="tweet">fasellus felis dolor@tempus eget lobortis id libero Donec scelerisque leo ac risus. <em>3 hours ago</em></p>
    <p class="tweet">fasellus felis dolor@tempus eget lobortis id libero Donec scelerisque leo ac risus. <em>3 hours ago</em></p>
    <p class="tweet">fasellus felis dolor@tempus eget lobortis id libero Donec scelerisque leo ac risus. <em>4 hours ago</em></p>
  </div>
  <div class="f-col">
    <h4>Main menu</h4>
    <ul><li>Home</li><li>Photo Gallery</li><li>FAQ's</li><li>Contact Us</li><li>Outdoorlasertag</li><li>Comparison of features</li><li>Online Booking</li><li>Blog</li><li>Testimonials</li></ul>
  </div>
  <div class="f-col">
    <h4>Usefull Links</h4>
    <ul><li>Sitemap</li><li>Terms &amp; Conditions</li><li>Privacy Policy</li><li>FAQ's</li><li>Latest News &amp; Updates</li><li>Recent Blog Posts</li><li>Newsletter</li></ul>
    <p style="font-size:6.5px;margin-top:6px">Follow us on</p>
    <div class="social"><span style="background:#4ea3f0"></span><span style="background:#e9a33a"></span><span style="background:#2f5fb0"></span><span style="background:#eb1f27"></span></div>
  </div>
  <div>
    <h4 style="font-size:9px;margin-bottom:5px">CONTACT US</h4>
    <div class="newsletter">
      <span class="tag">NEWSLETTER</span>
      <p><svg viewBox="0 0 12 10"><rect x=".5" y=".5" width="11" height="9" fill="none" stroke="#fff"/><path d="M.5.5 6 5l5.5-4.5" fill="none" stroke="#fff"/></svg>Receiving our new look monthly</p>
      <div class="field">Enter your email address</div>
      <span class="submit">SUBMIT</span>
    </div>
  </div>
</footer>

<div class="copyright">Copyright © 2014, www.glowarenaplay.com.my All rights reserved.</div>
</div>
</body>
</html>
```